Lionel Arbusto and Dwight Halvorsen Advertisement

We would like an ad that conveys understated elegance. We are a company that purchases estate jewelry watches and diamonds. We care to a wealthy, upscale clientele.

Target Market(s)

Wealthy upscale.

Industry/Entity Type

It Company

Requirements
Must have
• Elegant Design. Crisp Clean. Attached a doc of how the ad should be arranged.

```html
<!DOCTYPE html>
<html lang="en">
<head>
<meta charset="utf-8">
<title>Lionel Arbusto &amp; Dwight Halvorsen — Ready to Sell?</title>
<link rel="stylesheet" href="https://fonts.googleapis.com/css2?family=Roboto+Condensed:wght@300;400&family=Cinzel:wght@400&display=swap">
<style>
  :root {
    --paper: #e9e9ea;
    --paper-light: #f6f6f6;
    --paper-shade: #d4d4d6;
    --gold-deep: #b8860b;
    --gold: #d9a514;
    --gold-bright: #f3cf3a;
    --gold-text: #b98a14;
    --ink: #1d1d1d;
    --ink-soft: #333;
    --white: #ffffff;
  }
  * { margin: 0; padding: 0; box-sizing: border-box; }
  html, body { width: 800px; height: 1200px; overflow: hidden; background: var(--paper); }
  .ad {
    position: relative;
    width: 800px;
    height: 1200px;
    overflow: hidden;
    font-family: "Roboto Condensed", "Arial Narrow", sans-serif;
    background:
      linear-gradient(120deg, rgba(232,190,80,.35) 0%, rgba(255,255,255,0) 14%),
      linear-gradient(240deg, rgba(232,190,80,.35) 0%, rgba(255,255,255,0) 14%),
      radial-gradient(ellipse at 50% 45%, var(--paper-light) 0%, var(--paper) 55%, var(--paper-shade) 100%);
  }
  .ribbon { position: absolute; left: 165px; top: 0; width: 460px; height: 470px; filter: drop-shadow(0 10px 12px rgba(0,0,0,.3)); }
  .headline {
    position: absolute; left: 165px; top: 48px; width: 460px;
    text-align: center; color: var(--white); font-weight: 400;
    text-shadow: 0 2px 4px rgba(0,0,0,.35); line-height: 1;
  }
  .headline .big { display: block; font-size: 84px; letter-spacing: 1px; }
  .headline .small { display: block; font-size: 58px; margin: 6px 0 4px; font-weight: 300; }
  .gem {
    position: absolute; left: 290px; top: 455px; width: 270px; height: 250px;
    border-radius: 24px; transform: rotate(-4deg);
    background: radial-gradient(circle at 45% 40%, #ffffff 0%, #dcdcde 45%, #9d9da1 100%);
    box-shadow: 0 30px 40px -20px rgba(0,0,0,.35);
  }
  .promise { position: absolute; left: 0; width: 800px; text-align: center; }
  .promise-lead { top: 742px; font-size: 23px; color: var(--gold-text); }
  .promise-sub { top: 776px; font-size: 18px; color: var(--ink); }
  .brand-name {
    position: absolute; left: 0; top: 940px; width: 800px; text-align: center;
    font-family: "Cinzel", serif; font-size: 27px; letter-spacing: 1.5px; color: var(--ink-soft);
  }
  .tagline {
    position: absolute; left: 150px; top: 983px; width: 500px;
    display: flex; align-items: center; gap: 12px;
    font-family: "Cinzel", serif; font-size: 12px; letter-spacing: 2px; color: var(--ink-soft);
  }
  .tagline::before, .tagline::after { content: ""; flex: 1; height: 1px; background: var(--ink-soft); }
  .rule { position: absolute; left: 0; top: 1082px; width: 800px; height: 3px; background: var(--gold); }
  .plaque { position: absolute; left: 165px; top: 1026px; width: 495px; height: 138px; filter: drop-shadow(0 6px 8px rgba(0,0,0,.25)); }
  .contact {
    position: absolute; left: 165px; top: 1042px; width: 495px; text-align: center;
    color: var(--white); font-size: 18px; line-height: 26px; font-weight: 300;
  }
  .contact .reach { font-weight: 400; }
  .base-band {
    position: absolute; left: 0; bottom: 0; width: 800px; height: 18px;
    background: linear-gradient(90deg, var(--gold-deep), var(--gold-bright), var(--gold-deep), var(--gold-bright), var(--gold-deep));
  }
</style>
</head>
<body>
<main class="ad">
  <svg class="ribbon" viewBox="0 0 460 470" aria-hidden="true">
    <defs>
      <linearGradient id="goldSheen" x1="0" y1="0" x2="1" y2="1">
        <stop offset="0" stop-color="#c48b0c"/>
        <stop offset=".3" stop-color="#f2cd3c"/>
        <stop offset=".55" stop-color="#c99212"/>
        <stop offset=".8" stop-color="#f0c63a"/>
        <stop offset="1" stop-color="#b07c08"/>
      </linearGradient>
    </defs>
    <polygon points="0,0 460,0 460,460 230,310 0,460" fill="url(#goldSheen)"/>
    <polyline points="24,0 24,418 230,290 436,418 436,0" fill="none" stroke="#fff" stroke-width="2"/>
  </svg>
  <h1 class="headline">
    <span class="big">READY</span>
    <span class="small">TO</span>
    <span class="big">SELL?</span>
  </h1>

  <div class="gem" role="img" aria-label="Emerald-cut diamond resting on a pale grey surface"></div>

  <p class="promise promise-lead">Utmost Discretion</p>
  <p class="promise promise-sub">By Appointment</p>

  <p class="brand-name">Lionel Arbusto &amp; Dwight Halvorsen</p>
  <p class="tagline">YOUR BEST OPTION</p>

  <div class="rule"></div>
  <svg class="plaque" viewBox="0 0 495 138" aria-hidden="true">
    <defs>
      <linearGradient id="plaqueSheen" x1="0" y1="0" x2="1" y2="1">
        <stop offset="0" stop-color="#f0c63a"/>
        <stop offset=".45" stop-color="#c38d10"/>
        <stop offset=".75" stop-color="#efc43a"/>
        <stop offset="1" stop-color="#b57f08"/>
      </linearGradient>
    </defs>
    <polygon points="24,0 471,0 495,24 495,114 471,138 24,138 0,114 0,24" fill="url(#plaqueSheen)"/>
    <polygon points="30,10 465,10 485,30 485,108 465,128 30,128 10,108 10,30" fill="none" stroke="#fff" stroke-width="1.5" opacity=".85"/>
  </svg>
  <address class="contact" style="font-style:normal">
    Via Serena<br>
    118-B Larkspur Avenue, Palm Harbor, FL 34683<br>
    <span class="reach">concierge@arbhalv.com &bull; 727.555.0193</span>
  </address>

  <div class="base-band"></div>
</main>
</body>
</html>
```